Musician looking for catchy Web Design for promotion

My name is Brenna Colfer. I'm an Irish musician who plays the tin whistle and the flute. I'm also the leader of a traditional Irish music and dance ensemble called Wander the Hillside (www.wanderthehillside-example.com) and for the past 30 years, I've toured the world performing thousands of concerts. I run an annual cruise (www.brennacolfervoyage-example.com) that I would like a link to, and I'm also I'm organizing tours to Ireland that I would like a page set up for. I'm looking for a website to promote my tours and my music.
Updates

Hello Graphic Designers, I am only looking for the design of the home page to make my decision. Thank you. Brenna

Target Market(s)

Music fans of Irlsh and World Music

Industry/Entity Type

Entertainment Industry

Number of Pages Required

5+ page

Requirements
Must have
• I'm looking for a catchy design that shows a photo of me. I would like a few links....
• BIO
• TOURDATES
• BRENNA COLFER CRUISE
• MUSICAL TOUR OF IRELAND
• CONTACT
• VIDEO
• GALLERY
• CONTACT
• MAILING LIST
• STORE
Nice to have
• we'll see!

```html
<!DOCTYPE html>
<html lang="en">
<head>
<meta charset="utf-8">
<title>Brenna Colfer's Musical Tour of Ireland</title>
<link rel="stylesheet" href="https://fonts.googleapis.com/css2?family=Cinzel:wght@400;700&family=Great+Vibes&family=Open+Sans:ital,wght@0,400;0,600;0,700;1,400&display=swap">
<style>
:root{
  --ink:#111;
  --black:#000;
  --white:#fff;
  --gold:#8f7530;
  --gold-dark:#7d6427;
  --gold-light:#d2b14c;
  --gold-text:#a8862e;
  --line:#c9c9c9;
  --grey:#666;
  --footer:#0e0b12;
}
*{box-sizing:border-box;margin:0;padding:0}
html,body{width:1200px;height:2659px;overflow:hidden;background:var(--white)}
body{font-family:"Open Sans",Arial,sans-serif;color:var(--ink);position:relative}

/* header */
.site-header{position:absolute;left:0;top:0;width:1200px;height:135px;background:var(--white)}
.search{position:absolute;left:97px;top:56px;width:165px;height:36px;border:1px solid var(--line);border-radius:4px 14px 4px 4px;font-size:11px;color:#aaa;padding:10px 0 0 22px}
.brand{position:absolute;left:462px;top:44px;width:290px;height:56px;display:flex;align-items:center;gap:12px}
.brand-mark{width:36px;height:36px;border-radius:50%;background:var(--ink)}
.brand-name{font-family:"Cinzel",serif;font-weight:700;font-size:17px;line-height:1.2;color:var(--ink)}
.brand-name span{display:block;font-size:10.5px}
.cart{position:absolute;left:983px;top:61px;font-size:15px;font-weight:700}

/* nav */
.main-nav{position:absolute;left:0;top:135px;width:1200px;height:57px;background:var(--black)}
.main-nav a{position:absolute;top:0;height:57px;line-height:57px;color:var(--white);font-size:12px;text-decoration:none;text-transform:uppercase}
.main-nav a.active{background:var(--gold);padding:0 16px;margin-left:-16px}

/* hero */
.hero{position:absolute;left:0;top:192px;width:1200px;height:434px;overflow:hidden}
.hero-band{position:absolute;top:0;height:434px}
.hero-band.band-photo{left:0;width:526px;
  background:
    radial-gradient(ellipse 60px 200px at 85px 260px,rgba(10,10,10,.85),transparent 80%),
    radial-gradient(ellipse 55px 190px at 215px 250px,rgba(10,10,10,.8),transparent 80%),
    radial-gradient(ellipse 65px 200px at 340px 255px,rgba(10,10,10,.85),transparent 80%),
    radial-gradient(ellipse 55px 190px at 440px 250px,rgba(15,15,15,.8),transparent 80%),
    linear-gradient(90deg,#4a4a4a,#9d9d9d 30%,#6b6b6b 55%,#c4c4c4 80%,#555),
    #777}
.hero-band.portrait{left:526px;width:674px;
  background:
    radial-gradient(ellipse 150px 200px at 310px 180px,rgba(20,14,10,.9),transparent 80%),
    radial-gradient(ellipse 70px 80px at 320px 110px,rgba(205,160,130,.95),transparent 85%),
    radial-gradient(ellipse 120px 260px at 110px 200px,rgba(45,35,25,.8),transparent 80%),
    radial-gradient(ellipse 100px 240px at 560px 200px,rgba(40,38,30,.75),transparent 80%),
    linear-gradient(90deg,#a18f6e,#6d5c44 25%,#c9bf9f 60%,#e6e2cf 75%,#7f7a62),
    #8a7a5e}
.hero-caption{position:absolute;left:652px;top:278px;width:408px;height:110px;background:linear-gradient(90deg,rgba(60,60,60,.85),rgba(90,90,90,.7))}
.hero-caption .script{position:absolute;left:36px;top:2px;font-family:"Great Vibes",cursive;font-size:40px;color:var(--white)}
.hero-caption .name{position:absolute;left:78px;top:48px;font-family:"Cinzel",serif;font-size:34px;color:var(--white)}

/* about */
.about-art{position:absolute;left:97px;top:700px;width:488px;height:342px;border-radius:6px;box-shadow:6px 6px 8px rgba(0,0,0,.45);
  background:
    radial-gradient(ellipse 110px 90px at 340px 140px,rgba(232,196,40,.9),transparent 80%),
    linear-gradient(160deg,transparent 42%,rgba(40,28,20,.85) 45%,rgba(60,44,30,.85) 50%,transparent 53%),
    linear-gradient(135deg,#fdfdfd,#e4e6ee 55%,#c6cbd8)}
.about-kicker{position:absolute;left:613px;top:700px;font-family:"Great Vibes",cursive;font-size:40px;color:var(--gold-text)}
.about-title{position:absolute;left:655px;top:742px;font-family:"Cinzel",serif;font-size:36px}
.about-text{position:absolute;left:613px;top:822px;width:490px;font-size:13.3px;font-style:italic;line-height:17.5px}
.btn{position:absolute;background:var(--gold);color:var(--white);font-size:14px;text-align:center}
.btn.read{left:615px;top:973px;width:129px;height:39px;line-height:39px}

/* tours */
.tours{position:absolute;left:0;top:1102px;width:1200px;height:585px;background:radial-gradient(ellipse at 50% 0%,var(--gold-light),var(--gold) 55%,var(--gold-dark))}
.tours h2{position:absolute;left:0;top:48px;width:1200px;text-align:center;font-family:"Cinzel",serif;font-weight:400;font-size:34px;color:var(--ink)}
.tours .sub{position:absolute;left:0;top:101px;width:1200px;text-align:center;font-family:"Cinzel",serif;font-size:15px}
.album{position:absolute;top:148px;width:300px}
.album .art{height:299px;box-shadow:4px 6px 8px rgba(0,0,0,.35);position:relative}
.album .art.a1{background:
    radial-gradient(ellipse 90px 110px at 150px 110px,rgba(20,18,16,.9),transparent 80%),
    radial-gradient(ellipse 40px 120px at 40px 150px,rgba(30,28,24,.9),transparent 80%),
    radial-gradient(ellipse 40px 120px at 260px 150px,rgba(30,28,24,.9),transparent 80%),
    linear-gradient(160deg,#6a6456,#3a3631 60%,#25231f)}
.album .art.a2{background:
    radial-gradient(ellipse 120px 130px at 150px 240px,rgba(20,14,12,.95),transparent 80%),
    radial-gradient(ellipse 80px 90px at 150px 80px,rgba(60,35,20,.9),transparent 85%),
    linear-gradient(160deg,#c48a48,#9a6230 55%,#5a3a22)}
.album .art.a3{background:
    radial-gradient(ellipse 110px 120px at 150px 220px,rgba(60,90,85,.9),transparent 80%),
    radial-gradient(ellipse 80px 60px at 280px 150px,rgba(80,120,150,.8),transparent 80%),
    linear-gradient(180deg,#eef2f6,#c9d8e4 35%,#6f8f5e 60%,#3b4a3c)}
.album .btn.view{left:85px;top:200px;width:130px;height:39px;line-height:39px}
.album h3{margin-top:30px;text-align:center;font-size:22px;font-weight:700;color:var(--white)}
.album p{margin-top:2px;text-align:center;font-size:14px;font-style:italic;color:var(--white)}

/* contact */
.field{position:absolute;left:197px;width:395px;border:2px solid #d8d8d8;font-size:12px;padding:14px 0 0 10px}
.btn.submit{left:197px;top:2109px;width:163px;height:50px;line-height:50px;font-size:14px;box-shadow:1px 1px 2px rgba(0,0,0,.4)}
.address{position:absolute;left:610px;top:1750px;font-size:13px;line-height:22px}
.address strong{font-weight:400;font-size:15px}
.map{position:absolute;left:608px;top:1884px;width:438px;height:213px;border:1px solid var(--line);
  background:
    radial-gradient(ellipse 90px 50px at 120px 55px,rgba(160,196,228,.95),transparent 80%),
    radial-gradient(ellipse 80px 40px at 260px 20px,rgba(170,200,230,.9),transparent 80%),
    radial-gradient(ellipse 140px 160px at 440px 200px,rgba(160,196,228,.95),transparent 75%),
    radial-gradient(ellipse 150px 80px at 170px 150px,rgba(210,220,185,.9),transparent 85%),
    linear-gradient(135deg,#ece7da,#e2e3cf 55%,#dad7c2)}
.map-credit{position:absolute;right:4px;bottom:3px;font-size:8px;color:#444}

/* footer */
.site-footer{position:absolute;left:0;top:2224px;width:1200px;height:435px;background:radial-gradient(ellipse at 50% 40%,#2a1e22,var(--footer) 70%)}
.site-footer h2{position:absolute;left:0;top:50px;width:1200px;text-align:center;font-family:"Cinzel",serif;font-weight:400;font-size:36px;color:var(--white)}
.site-footer .time{position:absolute;left:0;top:111px;width:1200px;text-align:center;font-size:11px;color:#999}
.site-footer .feed{position:absolute;left:0;top:132px;width:1200px;text-align:center;font-size:19px;line-height:30px;color:var(--white)}
.follow{position:absolute;left:554px;top:203px;width:92px;height:18px;background:#e6e6e6;border-radius:2px;font-size:9px;line-height:18px;text-align:center;color:#333}
.social{position:absolute;top:274px;width:56px;height:56px;border-radius:50%;background:var(--white);color:var(--ink);font-size:9.5px;font-weight:700;text-align:center;line-height:56px}
.copyright{position:absolute;left:0;top:370px;width:1200px;text-align:center;font-size:12px;color:#ccc}
</style>
</head>
<body>

<header class="site-header">
  <div class="search">Search</div>
  <div class="brand">
    <div class="brand-mark"></div>
    <div class="brand-name">BRENNA COLFER'S<span>MUSICAL TOUR OF IRELAND</span></div>
  </div>
  <div class="cart">Shopping Cart (0)</div>
</header>

<nav class="main-nav">
  <a style="left:121px">Bio</a>
  <a class="active" style="left:174px">Tourdates</a>
  <a style="left:269px">Brenna Colfer Cruise</a>
  <a style="left:438px">Musical Tour of Ireland</a>
  <a style="left:622px">Contact</a>
  <a style="left:707px">Video</a>
  <a style="left:775px">Gallery</a>
  <a style="left:854px">Contact</a>
  <a style="left:943px">Mailing List</a>
  <a style="left:1044px">Store</a>
</nav>

<section class="hero">
  <div class="hero-band band-photo" role="img" aria-label="Black and white photo of the ensemble holding accordion, guitar, flute and fiddle"></div>
  <div class="hero-band portrait" role="img" aria-label="Colour portrait of Brenna Colfer beside a wrought iron gate"></div>
  <div class="hero-caption">
    <div class="script">Official Website</div>
    <div class="name">BRENNA COLFER'S</div>
  </div>
</section>

<section class="about">
  <div class="about-art" role="img" aria-label="Illustration of a yellow songbird perched on a wooden flute"></div>
  <div class="about-kicker">About Us</div>
  <div class="about-title">Brenna Colfer's</div>
  <p class="about-text"><strong>BRENNA COLFER</strong> is considered one of the greatest musicians and personalities in the history of Irish music in America. She was born in the Bronx, New York of Irish parents, and she is the second oldest of seven children raised in a musical household. Her mother Helen hails from Miltown Malbay, County Clare and her father Joe, an All-Ireland Champion accordion player, was a native of Portumna, County Galway.</p>
  <div class="btn read">Read More</div>
</section>

<section class="tours">
  <h2>Musical Tours of ireland</h2>
  <div class="sub">NEW ALBUM LIST</div>
  <div class="album" style="left:106px">
    <div class="art a1" role="img" aria-label="Darkened portrait photo by an iron gate"><div class="btn view">View Profile</div></div>
    <h3>Album Name</h3><p>place name where perform</p>
  </div>
  <div class="album" style="left:450px">
    <div class="art a2" role="img" aria-label="Portrait photo holding a flute"></div>
    <h3>Album Name</h3><p>place name where perform</p>
  </div>
  <div class="album" style="left:792px">
    <div class="art a3" role="img" aria-label="Outdoor photo playing a tin whistle by the sea"></div>
    <h3>Album Name</h3><p>place name where perform</p>
  </div>
</section>

<section class="contact">
  <div class="field" style="top:1751px;height:46px">FULL NAME</div>
  <div class="field" style="top:1810px;height:46px">EMAIL ID</div>
  <div class="field" style="top:1868px;height:46px">MOBILE NUMBER</div>
  <div class="field" style="top:1927px;height:168px">YOUR MESSAGE</div>
  <div class="btn submit">SUBMIT FORM</div>
  <div class="address">
    <strong>NEW YORK</strong><br>
    18 West 40th Street New York<br>
    212-555-0148<br>
    Email: info@domain.com
  </div>
  <div class="map" role="img" aria-label="Road map of the north-eastern United States"><span class="map-credit">Map data ©2014 Mapline</span></div>
</section>

<footer class="site-footer">
  <h2>We Are Social</h2>
  <div class="time">2 HOURS AGO</div>
  <div class="feed">Contrary to popular belief, Lorem Ipsum is not simply random text.<br>It has roots in a piece of classical Latin literature from 45 BC.</div>
  <div class="follow">Follow @chirper</div>
  <div class="social" style="left:500px">Chirper</div>
  <div class="social" style="left:575px">Friend</div>
  <div class="social" style="left:646px">Linkwork</div>
  <div class="copyright">Copyright © 2016. Loft Studio. All Right Reserved</div>
</footer>

</body>
</html>
```